Velmont Advisory e-Flyer Design

Need 6 or so one pagers done. To be used to email to clients. Each to look similar with slight variations. Attached is an example done for a completely different organization, but it has the style we are looking for, and it is energetic and corporate.

```html
<!DOCTYPE html>
<html lang="en">
<head>
<meta charset="utf-8">
<title>Velmont Advisory – One Pager</title>
<link href="https://fonts.googleapis.com/css2?family=Raleway:wght@300;400;500;600;700&display=swap" rel="stylesheet">
<style>
:root{
  --red:#d12027;
  --grey:#7b7b7c;
  --ink:#4a4a4a;
  --paper:#ffffff;
  --backdrop:#e4e4e4;
  --photo-a:#c9d3dd;
  --photo-b:#2f3e52;
}
*{margin:0;padding:0;box-sizing:border-box}
html,body{width:1200px;height:1200px;overflow:hidden}
body{background:var(--backdrop);font-family:"Raleway",sans-serif;position:relative}
.flyer{position:absolute;left:253px;top:30px;width:785px;height:1291px;background:var(--paper);transform:scale(0.884);transform-origin:0 0;overflow:hidden}
.top-band{position:absolute;left:0;top:57px;width:785px;height:78px;background:var(--grey)}
.brand{position:absolute;left:46px;top:23px;width:148px;height:139px;background:var(--red);color:#fff;display:flex;align-items:center;justify-content:center;text-align:center;font-weight:700;font-size:22px;line-height:1.15;padding:10px}
.tagline{position:absolute;left:222px;top:74px;color:#fff;font-weight:400;font-size:18.5px;line-height:28px}
.intro{position:absolute;left:46px;top:183px;width:420px;color:var(--ink)}
.intro h2{font-size:17px;font-weight:700;letter-spacing:.2px;margin-bottom:4px}
.intro p{font-size:12.6px;line-height:15.4px;text-align:justify;margin-bottom:5px;font-weight:400;letter-spacing:-.1px}
.intro .w1{width:420px}
.intro .w2{width:405px}
.intro .w3{width:388px}
.intro .w4{width:356px}
.intro .w5{width:318px}
.intro h2.gap{margin-top:17px}
.intro h2.gap-lg{margin-top:19px}
.photo{position:absolute;left:338px;top:193px;width:447px;height:367px;background:linear-gradient(135deg,var(--photo-a) 0%,#8ea0b4 45%,var(--photo-b) 100%);clip-path:polygon(162px 0,100% 0,100% 100%,0 100%)}
.services{position:absolute;left:0;top:573px;width:785px;height:642px;background:var(--red);color:#fff}
.services-tab{position:absolute;left:0;top:0}
.services-title{position:absolute;left:46px;top:9px;font-size:29px;font-weight:700}
.col{position:absolute;top:68px;width:332px}
.col.left{left:46px}
.col.right{left:407px}
.svc h3{font-size:17px;font-weight:700;line-height:18px}
.svc .lead{font-size:13px;line-height:15.4px;text-align:justify;margin-bottom:4px;letter-spacing:-.35px}
.svc ul{list-style:none;margin-bottom:16px}
.svc li{font-size:9.6px;line-height:12.2px;text-align:justify;padding-left:12px;position:relative;margin-bottom:5.5px}
.svc li::before{content:"•";position:absolute;left:2px;top:0}
.contact{position:absolute;left:46px;top:1225px;font-size:15px;color:var(--ink);line-height:19px}
.contact .hl{color:var(--red)}
</style>
</head>
<body>
<div class="flyer">
  <div class="top-band"></div>
  <div class="brand">Velmont Advisory</div>
  <p class="tagline">Velmont Advisory is a unique global management consultancy.<br>We convert strategy into action, and action into result</p>

  <section class="intro">
    <h2>WHO WE ARE</h2>
    <p class="w1">Velmont Advisory is a unique, global, management consultancy. We specialize in turning strategy into action, and action into results.</p>
    <p class="w2">Velmont Advisory operates in the US, Europe, Asia, Australia and New Zealand.</p>
    <p class="w3">The Velmont Advisory team consists of highly experienced corporate executives with a track record of delivering transformational programs to organizations across industries, both commercial and not for profit, large and small, to achieve dramatic performance improvement.</p>
    <p class="w4">Velmont Advisory uses a proven, proprietary method, Catalyst, to galvanize organizations to achieve higher performance.</p>
    <h2 class="gap">MISSION</h2>
    <p class="w5">To partner with organizations to ignite and empower them around a clear strategy, and facilitate efficient and fully integrated execution, to deliver higher performance.</p>
    <h2 class="gap-lg">VALUES</h2>
    <p>Ignite, Empower, Deliver</p>
  </section>

  <div class="photo" role="img" aria-label="Photo of two businessmen in suits reviewing a tablet together"></div>

  <section class="services">
    <svg class="services-tab" width="246" height="49" viewBox="0 0 246 49"><polygon points="0,0 246,0 218,49 0,49" fill="var(--grey)"/></svg>
    <div class="services-title">SERVICES</div>

    <div class="col left">
      <div class="svc">
        <h3>CATALYST</h3>
        <p class="lead">Catalyst is a proven, proprietary method to bring cohesion to a team to create a shared understanding of what they want to achieve and how they will galvanize the organization to achieve it.</p>
        <ul>
          <li>Effective dialogue is the most productive way to truly harness the collective intellect of a team and the organization</li>
          <li>Velmont Advisory uses a tested process, Catalyst, to create a space for great dialogue for teams of up to 300 people</li>
          <li>The Catalyst process is tailored for each client to clarify strategy, define the execution path, strengthen team cohesion and ignite momentum</li>
          <li>Catalyst happens at speed to create a bridge for the present state to the future state</li>
          <li>Catalyst is purposely built to create ownership by the team</li>
          <li>Catalyst frequently produces break throughs and is about unleashing what a collective can achieve together</li>
        </ul>
      </div>
      <div class="svc">
        <h3>STRATEGY CLARIFICATION</h3>
        <p class="lead">Knowing what the organization wants to be in 3-5 years time is a competitive advantage</p>
        <ul>
          <li>Consciously exploring the alternatives and selecting an objective and strategy for the strategic horizon is a competitive advantage for organizations that undertake a proper strategic planning process including understanding evolving customer needs, competitive differentiation, and the critical capabilities required to compete and win</li>
          <li>Research shows that organizations that are executing against a clear strategy out perform those that do not, even if the choice of strategy ultimately proves to be incorrect, largely due to deliberate intent and discipline</li>
          <li>Having a 3-5 year strategy is critical to allowing the organization to have a coherent direction which all stakeholders can support, make strategic investments in future capabilities, and out perform the competition</li>
        </ul>
      </div>
    </div>

    <div class="col right">
      <div class="svc">
        <h3>EXECUTIONAL ALIGNMENT</h3>
        <p class="lead">Strategy is just an exercise unless it is executed effectively and becomes the operating blueprint of the organization</p>
        <ul>
          <li>Strategy is a critical starting point to set objective and direction for the 3 year horizon, however without the organization executing against this strategy, it is academic</li>
          <li>Driving executional alignment to the strategy is critical to success, and requires the organization to consciously align the operations of the business to the strategy</li>
          <li>Executional alignment requires over coming the inertia of Business as Usual by enabling change through all aspects of the organization, identifying and removing barriers, beginning with a culture of embracing the strategy and competing to win</li>
        </ul>
      </div>
      <div class="svc">
        <h3>LEADERSHIP DEVELOPMENT</h3>
        <p class="lead">Having the right leadership capability is the difference between success and failure</p>
        <ul>
          <li>Every organization is comprised of unique people with different styles, experience and expertise</li>
          <li>Ensuring leaders at all levels of the organization are suitably developed and equipped to do the best job is critical to out performing the competition and being an employer of choice to retain talented employees</li>
          <li>The skills of leadership are evolving with changing demographics, technology, increased understanding of the benefits of diversity, a premium on innovation, amongst other macro trends, and organizations need to ensure their leaders have the knowledge and capabilities to manage these changes effectively</li>
        </ul>
      </div>
      <div class="svc">
        <h3>CULTURAL TRANSFORMATION</h3>
        <p class="lead">Organizational culture can evolve organically, or it can be seen as a business asset that is consciously managed</p>
        <ul>
          <li>Organizations that choose the culture they desire are leveraging one of the most important business assets available, one that is often left to evolve without overt consideration</li>
          <li>Placing clear focus on the desired culture and having initiatives to achieve this, and monitoring performance against the intent, is a competitive differentiator</li>
        </ul>
      </div>
    </div>
  </section>

  <div class="contact">
    For more information:<br>
    CALL <span class="hl">+1 212 555 0147</span>, Email <span class="hl">info@velmontadvisory.com</span>
  </div>
</div>
</body>
</html>
```